Bramblewick Co Leaflet. A5 2-sided Flyer for a UK Lawn Treatment Company

I need an A5 two-side leaflet / flyer designed for my Lawn Treatment company. The leaflet will be for door-drops so quick impact needed. Full colour, both sides. I provide lawn treatments to customers in the Exeter area of Devon. I would like to design to be clear, fresh and reflect the joy a good lawn and garden can bring.

Target Market(s)

Home Owners. 30-80 Years. Familys

Font styles to use
Sans Serif

Colors
9bcb3c
f78f20
ec1f27
33a6d7

Requirements
Must have
• Good front page picture
• Logo
• Contact details on front.
• Call to Action
• More details in Text file included in design.
Nice to have
• Clipart of a family / lady enjoying a lawn.

```html
<!DOCTYPE html>
<html lang="en">
<head>
<meta charset="utf-8">
<title>Bramblewick Co – Lawn Treatments Leaflet</title>
<link href="https://fonts.googleapis.com/css2?family=Arimo:wght@400;700&family=Roboto+Slab:wght@400;500;600&display=swap" rel="stylesheet">
<style>
  :root {
    --green: #3b9a17;
    --green-dark: #2f8a10;
    --ink: #111111;
    --paper: #ffffff;
    --grass-light: #e6f1d6;
    --grass-mid: #b9d98e;
    --grass-deep: #8dbf5a;
  }
  html, body { margin: 0; padding: 0; overflow: hidden; background: var(--paper); }
  .leaflet {
    position: relative;
    width: 846px; height: 1200px;
    overflow: hidden;
    background: var(--paper);
    font-family: "Arimo", Arial, sans-serif;
    color: var(--ink);
  }
  .grass-backdrop {
    position: absolute; left: 0; right: 0; top: 480px; bottom: 0;
    background:
      radial-gradient(ellipse at 20% 100%, rgba(141,191,90,.75), transparent 60%),
      radial-gradient(ellipse at 85% 95%, rgba(170,210,120,.6), transparent 55%),
      linear-gradient(to bottom, var(--paper) 0%, var(--grass-light) 35%, var(--grass-mid) 75%, var(--grass-deep) 100%);
  }
  .feature { position: absolute; width: 340px; }
  .feature h2 {
    margin: 0;
    font-family: "Roboto Slab", Georgia, serif;
    font-weight: 400; font-size: 19.5px; line-height: 24px;
    color: var(--green);
  }
  .feature p { margin: 0; font-size: 17.4px; line-height: 24.3px; }
  .col-left { left: 49px; }
  .col-right { left: 460px; }
  .row-one { top: 39px; }
  .row-two { top: 252px; }
  .divider {
    position: absolute; left: 49px; top: 238px;
    width: 748px; height: 1px; background: var(--green);
  }
  .services {
    position: absolute; left: 460px; top: 252px; width: 330px;
    margin: 0; font-weight: 700; font-size: 17.6px; line-height: 24.3px;
  }
  .services .sep { color: var(--green); font-weight: 400; }
  .headline {
    position: absolute; left: 0; right: 0; top: 430px; margin: 0;
    text-align: center;
    font-family: "Roboto Slab", Georgia, serif;
    font-weight: 600; font-size: 27px; color: var(--green);
  }
  .photo {
    position: absolute; top: 528px; width: 336px; height: 196px;
  }
  .photo-before { left: 49px; background: linear-gradient(to bottom, #2f4a22 0%, #4d6a33 35%, #b7b84a 55%, #a7ab3c 100%); }
  .photo-after { left: 460px; width: 337px; background: linear-gradient(to bottom, #1f3a1a 0%, #3c6a2c 35%, #5fb737 55%, #4fa52c 100%); }
  .caption {
    position: absolute; top: 732px; margin: 0;
    font-size: 18px; line-height: 22px;
  }
  .caption .brand { color: var(--green); font-family: "Roboto Slab", Georgia, serif; }
  .testimonial {
    position: absolute; width: 340px; margin: 0;
    text-align: center; font-size: 17.4px; line-height: 24.3px;
  }
  .testimonial cite { font-style: normal; color: var(--green); }
  .t-1 { left: 47px; top: 794px; }
  .t-2 { left: 47px; top: 963px; }
  .t-3 { left: 458px; top: 794px; }
  .t-4 { left: 458px; top: 915px; }
  .contact-bar {
    position: absolute; left: 73px; right: 60px; top: 1124px;
    display: flex; justify-content: space-between;
    font-family: "Roboto Slab", Georgia, serif; font-size: 23px;
  }
  .contact-bar strong { font-weight: 500; }
</style>
</head>
<body>
<main class="leaflet">
  <div class="grass-backdrop" role="img" aria-label="Soft-focus close-up of green grass blades fading into the page"></div>

  <section class="feature col-left row-one">
    <h2>I will understand your lawn</h2>
    <p>Every lawn is unique. I take time to gain a comprehensive understanding of your lawn and its situation. I will also listen to you and understand your problems and your aspirations for your grass.</p>
  </section>

  <section class="feature col-right row-one">
    <h2>Your lawn treatments</h2>
    <p>I will create a custom treatment programme tailored to your lawn. I may also recommend some remedial treatments to correct any existing problems. There is no contract to sign. I guarantee all treatments.</p>
  </section>

  <div class="divider"></div>

  <section class="feature col-left row-two">
    <h2>Industry-leading lawn care</h2>
    <p>I have 8 years of experience in the leading edge of domestic lawn care. I have a comprehensive range of treatments including:</p>
  </section>

  <p class="services">Scarification <span class="sep">I</span> Aeration <span class="sep">I</span> Moss Control <span class="sep">I</span> Overseeding <span class="sep">I</span> Top Dressing <span class="sep">I</span> Lawn Repairs <span class="sep">I</span> Fertilisation &amp; Weed Control Pest and Disease Management <span class="sep">I</span> Special Event Preparation</p>

  <h1 class="headline">Save time and money and leave your lawn to an expert.</h1>

  <div class="photo photo-before" role="img" aria-label="Garden lawn before treatment, patchy yellow-green grass with trees and a cottage behind"></div>
  <div class="photo photo-after" role="img" aria-label="The same garden lawn after treatment, lush bright green grass"></div>

  <p class="caption" style="left:49px;">Before <span class="brand">BRAMBLEWICK CO</span></p>
  <p class="caption" style="left:460px;">After <span class="brand">BRAMBLEWICK CO</span></p>

  <blockquote class="testimonial t-1">We are so grateful for your skill over the years. We've seen our lawn thrive and you changed a neglected difficult garden to one that everyone comments on. <cite>- Morwenna</cite></blockquote>
  <blockquote class="testimonial t-2">We have very much appreciated your service over the last four years, and especially value your reliability and perennial cheerfulness! <cite>- Ambrose</cite></blockquote>
  <blockquote class="testimonial t-3">My lawn has never looked better since the day that you started to look after it for me. <cite>- Mr. Pellow</cite></blockquote>
  <blockquote class="testimonial t-4">Your company have been fantastic. Reliable, good advice, effective treatments and you are very knowledgeable about lawns. You really do know what you are talking about! Cannot recommend you highly enough. <cite>- Gareth</cite></blockquote>

  <footer class="contact-bar">
    <span>call <strong>01392 555718</strong></span>
    <span>text <strong>07700 900462</strong></span>
    <strong>bramblewick.co.uk</strong>
  </footer>
</main>
</body>
</html>
```